Custom Home Builder Needs a Website

Harbor Stone Builders Ltd. requires a clean professional 5 page website - Home, About Us, Gallery (Interior and Exterior), Our Process and Contact Us(with registration form). We are a home builder who also has homes for sale. Also please have a place for video embedding. Editable fields by user. Using the stationery 'feel' that is attached. Need social media links. If you require any additional files, please request.

Target Market(s)

Families and professionals

Industry/Entity Type

Home Builder

Coding

Coded - Design and coding required

Number of Pages Required

5+ page

Font styles to use
Sans Serif
Other font styles liked:
• Lato

Requirements
Must have
• Editable by user
• Register Button
• Place to put home models for sale - preferably on the first page
• 5 page website -
• -Home
• -About Us
• -Gallery (Interior and Exterior)
• -Our Process
• -Contact Us.
Nice to have
• Themed similar to current stationery
• place for video embedding
• Try some darker backgrounds
• Change pictures to B/W if works for design
Should not have
• cartoonish type of content

```html
<!DOCTYPE html>
<html lang="en">
<head>
<meta charset="utf-8">
<title>Harbor Stone Builders Ltd.</title>
<link href="https://fonts.googleapis.com/css2?family=Lato:wght@300;400;700&display=swap" rel="stylesheet">
<style>
:root{
  --green:#43a03a;
  --green-dark:#358a2e;
  --ink:#222;
  --muted:#777;
  --dark:#1a1a1a;
  --darker:#141414;
  --panel:#2a2a2a;
  --light:#f2f2f2;
  --rule:#e4e4e4;
  --white:#fff;
}
*{box-sizing:border-box;margin:0;padding:0}
html,body{width:1200px;height:3846px;overflow:hidden}
body{font-family:'Lato',sans-serif;color:var(--ink);background:var(--white);position:relative}
.abs{position:absolute}
.btn{position:absolute;display:flex;align-items:center;justify-content:center;background:var(--green);color:var(--white);font-size:12px;font-weight:400;border-radius:2px}

/* header */
.site-header{top:0;left:0;width:1200px;height:97px;background:var(--dark)}
.brand{left:97px;top:24px;display:flex;align-items:center;gap:10px}
.brand-mark{width:26px;height:26px;background:var(--green)}
.brand-name{color:var(--green);font-size:17px;font-weight:700;letter-spacing:1px;line-height:1.1;text-transform:uppercase}
.contact-call{left:569px;top:28px;display:flex;gap:12px;align-items:center;color:var(--white)}
.contact-call .icon{width:34px;height:34px;border:2px solid var(--green);border-radius:50%;display:flex;align-items:center;justify-content:center}
.contact-call strong{display:block;font-size:19px;font-weight:400}
.contact-call span{display:block;font-size:12px;color:#ccc;text-decoration:underline}
.btn-login{left:861px;top:28px;width:77px;height:41px;background:transparent;border:1px solid var(--green);font-size:14px}
.btn-register{left:964px;top:28px;width:133px;height:41px;font-size:14px}

/* hero */
.hero{top:97px;left:0;width:1200px;height:441px;background:var(--dark)}
.hero-photo{left:97px;top:0;width:1005px;height:441px;background:linear-gradient(180deg,#9a9a9a 0%,#6a6a6a 45%,#3a3a3a 75%,#555 100%)}
.hero-title{left:0;width:1200px;top:158px;text-align:center;color:var(--white);font-size:48px;font-weight:300;letter-spacing:9px}
.hero-sub{left:0;width:1200px;top:216px;text-align:center;color:var(--white);font-size:22px;font-weight:400;letter-spacing:6px}
.hero .btn{left:531px;top:272px;width:141px;height:34px;font-size:13px}
.social-rail{left:41px;top:147px;display:flex;flex-direction:column;gap:8px}
.social-rail i{display:block;width:20px;height:20px;border-radius:50%;background:#bbb}
.social-rail i:nth-child(2){background:var(--green)}
.menu-toggle{left:1141px;top:213px}

/* section heads */
.section-head{left:0;width:1200px;text-align:center}
.section-head h2{display:inline-block;font-size:28px;font-weight:400;padding:0 30px;background:linear-gradient(transparent 62%,var(--rule) 62%,var(--rule) 80%,transparent 80%)}
.section-head p{font-size:13px;color:var(--muted);margin-top:4px}

/* about */
.about-text{left:246px;top:679px;width:334px;font-size:12.5px;line-height:1.55;color:#555}
.about-text h3{font-size:14px;font-weight:700;color:var(--ink);margin-bottom:12px}
.about-text p{margin-bottom:12px}
.about .btn{left:246px;top:905px;width:123px;height:33px}
.video-frame{left:610px;top:677px;width:344px;height:269px;background:linear-gradient(160deg,#8fa7bd 0%,#3d5168 55%,#1f2a36 100%)}
.play{left:762px;top:791px;width:42px;height:42px;border:2px solid var(--white);border-radius:50%}
.play::after{content:"";position:absolute;left:15px;top:11px;border-left:14px solid var(--white);border-top:9px solid transparent;border-bottom:9px solid transparent}

/* listings */
.listings{top:1008px;left:0;width:1200px;height:556px;background:var(--light)}
.card{position:absolute;top:136px;width:269px;height:307px;background:var(--white);box-shadow:0 1px 4px rgba(0,0,0,.08)}
.card-photo{height:146px;position:relative}
.badge{position:absolute;left:0;bottom:0;background:var(--green);color:var(--white);font-size:10px;padding:3px 8px;font-weight:700}
.card-body{padding:14px 22px}
.card-body small{font-size:11px;color:var(--muted)}
.card-body h4{font-size:14px;font-weight:700;margin-top:4px}
.card-body .addr{font-size:11px;color:var(--muted)}
.card-body .price{font-size:14px;color:#c62828;font-weight:700;margin:12px 0 14px}
.card-body .specs{font-size:11px;color:var(--muted);border-top:1px solid var(--rule);padding-top:10px}
.arrow-nav{top:285px}
.listings .btn{left:536px;top:477px;width:136px;height:30px}

/* what we do */
.services{top:1654px;left:0;width:1200px;height:328px;background:var(--darker)}
.service{position:absolute;top:0;width:213px;height:328px;background:#262626;color:#ddd}
.service h4{height:56px;display:flex;align-items:center;justify-content:center;font-size:14px;font-weight:400;background:#333;color:var(--white)}
.service .shot{height:154px}
.service p{font-size:11px;line-height:1.45;text-align:center;padding:10px 14px}
.service .more{position:absolute;left:86px;bottom:-22px;width:42px;height:42px;border-radius:50%;background:var(--green);color:var(--white);font-size:10px;display:flex;align-items:center;justify-content:center}
.service.active{background:var(--green);top:-8px;height:336px;color:var(--white)}
.service.active h4{background:var(--green)}
.service.active .more{background:#111;bottom:-26px}
.service.active .more::after{content:"";width:7px;height:7px;border-radius:50%;background:var(--white)}

/* process */
.step{position:absolute;top:2160px;width:200px;text-align:center}
.step svg{display:block;margin:0 auto 14px}
.step h4{font-size:14px;font-weight:400}
.step p{font-size:11px;color:var(--muted);line-height:1.35;margin-top:6px;padding:0 22px}
.step-arrow{top:2190px}

/* projects */
.tile{position:absolute}
.tile-overlay{background:rgba(20,20,20,.88);color:var(--white);text-align:center}
.tile-overlay h5{font-size:15px;font-weight:400;margin-top:108px}
.tile-overlay p{font-size:12px;margin-top:6px;color:#ccc}

/* cta */
.cta-title{left:0;width:1200px;top:3158px;text-align:center;color:var(--green);font-size:30px;font-weight:700}
.cta-sub{left:0;width:1200px;top:3198px;text-align:center;font-size:16px;color:#444}

/* contact */
.contact{top:3349px;left:0;width:600px;height:420px;background:var(--dark);color:var(--white)}
.contact h3{position:absolute;left:172px;top:56px;font-size:15px;font-weight:700}
.field{position:absolute;border-bottom:1px solid #555;font-size:11px;color:#999;padding-bottom:10px}
.map{left:600px;top:3349px;width:600px;height:420px;background:linear-gradient(135deg,#e4e4e4,#cfcfcf 60%,#dadada)}

/* footer */
.site-footer{top:3769px;left:0;width:1200px;height:77px;background:var(--panel);color:#aaa;font-size:12px}
.site-footer .copy{left:172px;top:31px}
.site-footer nav{left:403px;top:31px;display:flex;gap:26px}
.footer-social{left:783px;top:28px;display:flex;gap:6px}
.footer-social i{display:block;width:22px;height:22px;border-radius:50%;background:#bbb}
.footer-social i:nth-child(2){background:var(--green)}
.to-top{left:1070px;top:18px;width:40px;height:40px;border:1px solid var(--green)}
</style>
</head>
<body>

<header class="abs site-header">
  <div class="abs brand"><span class="brand-mark"></span><span class="brand-name">Harbor Stone<br>Builders</span></div>
  <div class="abs contact-call">
    <span class="icon"><svg width="16" height="16" viewBox="0 0 24 24"><path d="M6 2l4 4-2 3c1 3 4 6 7 7l3-2 4 4-3 4C10 21 3 14 2 5z" fill="#43a03a"/></svg></span>
    <div><strong>Call:555.010.2040</strong><span>hello@harborstonebuilders.ca</span></div>
  </div>
  <a class="btn btn-login">Login</a>
  <a class="btn btn-register">Register Now</a>
</header>

<section class="abs hero">
  <div class="abs hero-photo" role="img" aria-label="Black and white photo of a modern two-storey home with a double garage"></div>
  <div class="abs social-rail"><i></i><i></i><i></i><i></i><i></i><i></i></div>
  <h1 class="abs hero-title">Design &amp; Build</h1>
  <p class="abs hero-sub">for Better Living</p>
  <a class="btn">Explore More</a>
  <svg class="abs menu-toggle" width="20" height="16" viewBox="0 0 20 16"><rect y="0" width="20" height="3" fill="#fff"/><rect y="6.5" width="20" height="3" fill="#fff"/><rect y="13" width="20" height="3" fill="#fff"/></svg>
</section>

<section class="about">
  <div class="abs section-head" style="top:596px"><h2>Harbor Stone Builders Ltd.</h2><p>Over the past 25 years in construction</p></div>
  <div class="abs about-text">
    <h3>Discover About Us</h3>
    <p>Our projects start with a vision, with a priority to build attractive, appealing and functional homes. To build the home that suits you best, we will spend time getting to know you and your family, with your specific wants and needs.</p>
    <p>Our goal is to put the same thought and care in every project that we would put into our own home. With our professional construction services, we strive for excellence in quality, functionality, sustainability and livability in every construction project ...</p>
  </div>
  <a class="btn">Discover More</a>
  <div class="abs video-frame" role="img" aria-label="Video still of a glass tower under construction with a crane"></div>
  <div class="abs play"></div>
</section>

<section class="abs listings">
  <div class="abs section-head" style="top:56px"><h2>Recent Property Listings</h2><p>See our recent listing here, you will find all kinds of homes.</p></div>
  <svg class="abs arrow-nav" style="left:98px" width="30" height="16" viewBox="0 0 30 16"><path d="M30 8H3M9 2L3 8l6 6" stroke="#aaa" stroke-width="2" fill="none"/></svg>
  <svg class="abs arrow-nav" style="left:1072px" width="30" height="16" viewBox="0 0 30 16"><path d="M0 8h27M21 2l6 6-6 6" stroke="#555" stroke-width="2" fill="none"/></svg>

  <article class="card" style="left:172px">
    <div class="card-photo" role="img" aria-label="Waterfront holiday home at dusk" style="background:linear-gradient(180deg,#6d93b8,#c7a77a 70%,#4a6b86)"><span class="badge">SALE</span></div>
    <div class="card-body"><small>House</small><h4>Lifestyle or Holiday Home</h4><div class="addr">(Baywood Heights 4012 )</div><div class="price">Price: $50,000.00</div><div class="specs">2500Sq.ft &nbsp;/ &nbsp;4 Bedroom &nbsp;/ &nbsp;3 Bath</div></div>
  </article>
  <article class="card" style="left:464px">
    <div class="card-photo" role="img" aria-label="Modern apartment villa building" style="background:linear-gradient(180deg,#9fb9d3,#d9d4c6 60%,#7a8a6a)"><span class="badge">SALE</span></div>
    <div class="card-body"><small>Villa</small><h4>Freedom, Space &amp; Solitude</h4><div class="addr">(Baywood Heights 4012 )</div><div class="price">Price: $50,000.00</div><div class="specs">2500Sq.ft &nbsp;/ &nbsp;4 Bedroom &nbsp;/ &nbsp;3 Bath</div></div>
  </article>
  <article class="card" style="left:756px">
    <div class="card-photo" role="img" aria-label="Large family home lit at twilight" style="background:linear-gradient(180deg,#3b4f8a,#8a7ab0 50%,#4f6a3e)"><span class="badge">SALE</span></div>
    <div class="card-body"><small>Family Home</small><h4>Lifestyle or Holiday Home</h4><div class="addr">(Baywood Heights 4012 )</div><div class="price">Price: $50,000.00</div><div class="specs">2500Sq.ft &nbsp;/ &nbsp;4 Bedroom &nbsp;/ &nbsp;3 Bath</div></div>
  </article>
  <a class="btn">View All Property</a>
</section>

<div class="abs section-head" style="top:1572px"><h2>What We Do</h2><p>Our primary business function is new home construction</p></div>
<section class="abs services">
  <div class="service" style="left:174px"><h4>New Home Build</h4><div class="shot" role="img" aria-label="Timber house frame under construction" style="background:linear-gradient(180deg,#8fb3d6,#c79a5a 60%,#7a5a34)"></div><p>Our primary business function is new home construction. Our vast experience will give you the home that you want ...</p><span class="more">More</span></div>
  <div class="service active" style="left:387px"><h4>Land Development</h4><div class="shot" role="img" aria-label="Excavator preparing a building lot" style="background:linear-gradient(180deg,#b6c9d8,#d9b45a 55%,#8a6b3a)"></div><p>An opportunity to bring value to our purchasers is to develop our lots or townhome projects ourselves. HSB's ...</p><span class="more"></span></div>
  <div class="service" style="left:600px"><h4>Renovations</h4><div class="shot" role="img" aria-label="Carpentry tools on a wooden workbench" style="background:linear-gradient(135deg,#7a5530,#c49a5e 60%,#5a3d22)"></div><p>We don't always want to move. Sometimes the area in which we live has so much going for it, the perfect lot size, ...</p><span class="more">More</span></div>
  <div class="service" style="left:813px"><h4>Partnerships</h4><div class="shot" role="img" aria-label="Business partners reviewing plans at a desk" style="background:linear-gradient(135deg,#d8dde3,#7d8a99 60%,#2f3a48)"></div><p>Occasionally people take on projects that may be a little too much for them. HSB can help you get ...</p><span class="more">More</span></div>
</section>

<section class="process">
  <div class="abs section-head" style="top:2060px"><h2>Our Process</h2><p>We design and bild home for you</p></div>
  <div class="step" style="left:100px"><svg width="52" height="48" viewBox="0 0 52 48" fill="none" stroke="#666" stroke-width="2"><path d="M12 22c-6 0-8-8-2-10 1-6 10-8 13-2 5-3 12 0 11 6 6 1 6 10-1 10"/><path d="M16 30l10-9 10 9v14H16z"/><rect x="23" y="36" width="6" height="8"/></svg><h4>The Dream</h4><p>Most building a new home to be an exciting journey</p></div>
  <div class="step" style="left:297px"><svg width="52" height="48" viewBox="0 0 52 48" fill="none" stroke="#666" stroke-width="2"><path d="M14 4h18l8 8v32H14z"/><path d="M32 4v8h8M20 20h14M20 27h14M20 34h9"/></svg><h4>The Design</h4><p>Your needs, ideas, &amp; dreams for your home</p></div>
  <div class="step" style="left:497px"><svg width="52" height="48" viewBox="0 0 52 48" fill="none" stroke="#666" stroke-width="2"><path d="M12 22a14 14 0 0 1 28 0"/><path d="M8 22h36v5H8zM26 8v8M14 44c0-8 5-12 12-12s12 4 12 12z"/></svg><h4>The Build</h4><p>We ensure that built to the standards</p></div>
  <div class="step" style="left:697px"><svg width="52" height="48" viewBox="0 0 52 48" fill="none" stroke="#666" stroke-width="2"><path d="M8 16h34M34 8l8 8-8 8M44 32H10M18 24l-8 8 8 8"/></svg><h4>The Move</h4><p>We make sure everything is what you wanted</p></div>
  <div class="step" style="left:897px"><svg width="52" height="48" viewBox="0 0 52 48" fill="none" stroke="#666" stroke-width="2"><path d="M10 20h8v24h-8zM18 22l8-16c4 0 5 3 4 8l-1 4h12c3 0 4 3 3 5l-4 17c-1 3-3 4-6 4H18"/></svg><h4>Warranty &amp; Beyond</h4><p>We are offering second to none client care</p></div>
  <svg class="abs step-arrow" style="left:288px" width="20" height="10" viewBox="0 0 20 10"><path d="M0 5h16M12 1l4 4-4 4" stroke="#43a03a" stroke-width="1.5" fill="none"/></svg>
  <svg class="abs step-arrow" style="left:487px" width="20" height="10" viewBox="0 0 20 10"><path d="M0 5h16M12 1l4 4-4 4" stroke="#43a03a" stroke-width="1.5" fill="none"/></svg>
  <svg class="abs step-arrow" style="left:687px" width="20" height="10" viewBox="0 0 20 10"><path d="M0 5h16M12 1l4 4-4 4" stroke="#43a03a" stroke-width="1.5" fill="none"/></svg>
  <svg class="abs step-arrow" style="left:887px" width="20" height="10" viewBox="0 0 20 10"><path d="M0 5h16M12 1l4 4-4 4" stroke="#43a03a" stroke-width="1.5" fill="none"/></svg>
  <a class="btn" style="left:536px;top:2336px;width:128px;height:28px">Explore More</a>
</section>

<section class="projects">
  <div class="abs section-head" style="top:2418px"><h2>Projects</h2><p>Discover our recent works</p></div>
  <div class="tile" style="left:0;top:2505px;width:559px;height:292px;background:linear-gradient(180deg,#cfd6dc,#5a5a5a 55%,#6f7a5c)" role="img" aria-label="Grey two-storey home with gabled roofs"></div>
  <div class="tile" style="left:564px;top:2505px;width:315px;height:292px;background:linear-gradient(180deg,#6b5a48,#3a2f26)" role="img" aria-label="Kitchen interior"></div>
  <div class="tile tile-overlay" style="left:564px;top:2505px;width:315px;height:292px"><h5>Interior</h5><p>Creative Gallery Kitchen Designs<br>Lakeside</p><svg style="margin-top:14px" width="16" height="16" viewBox="0 0 16 16" fill="none" stroke="#43a03a" stroke-width="2"><path d="M1 5V1h4M11 1h4v4M15 11v4h-4M5 15H1v-4"/></svg></div>
  <div class="tile" style="left:884px;top:2505px;width:316px;height:292px;background:linear-gradient(180deg,#c9d8e6,#8b8f8a 50%,#5f7f45)" role="img" aria-label="Suburban home with front lawn"></div>
  <div class="tile" style="left:0;top:2802px;width:438px;height:295px;background:linear-gradient(135deg,#a8a8a8,#6a6a6a 50%,#b33 80%,#444)" role="img" aria-label="Kitchen with mosaic backsplash and red kettle on the stove"></div>
  <div class="tile" style="left:443px;top:2802px;width:313px;height:295px;background:linear-gradient(180deg,#d7dde3,#6d6660 55%,#8a8076)" role="img" aria-label="Stone and siding home exterior with garage"></div>
  <div class="tile" style="left:761px;top:2802px;width:439px;height:295px;background:linear-gradient(135deg,#b9d0dc,#e8e6e2 55%,#e6a6c4)" role="img" aria-label="Bright child's bedroom with pastel walls"></div>
</section>

<h2 class="abs cta-title">Are you ready to start your project now</h2>
<p class="abs cta-sub">Our expert buiders will transform your home</p>
<a class="btn" style="left:505px;top:3249px;width:192px;height:36px">Start Your Project Now</a>

<section class="abs contact">
  <h3>Keep in touch with us</h3>
  <div class="field" style="left:172px;top:100px;width:344px">Name</div>
  <div class="field" style="left:172px;top:156px;width:200px">Email</div>
  <div class="field" style="left:400px;top:156px;width:116px">Phone</div>
  <div class="field" style="left:172px;top:212px;width:344px;height:86px">Message</div>
  <a class="btn" style="left:172px;top:328px;width:92px;height:28px"><svg width="12" height="10" viewBox="0 0 12 10" style="margin-right:6px"><path d="M0 0l12 5-12 5 2-5z" fill="#fff"/></svg>Send</a>
</section>
<div class="abs map" role="img" aria-label="Grey road map of the office area"></div>
<svg class="abs" style="left:885px;top:3521px" width="30" height="40" viewBox="0 0 30 40"><path d="M15 0C7 0 1 6 1 14c0 10 14 26 14 26s14-16 14-26C29 6 23 0 15 0z" fill="#43a03a"/><circle cx="15" cy="14" r="5" fill="#fff"/></svg>

<footer class="abs site-footer">
  <span class="abs copy">© 2016 Harbor Stone Builders Ltd.</span>
  <nav class="abs"><span>About</span><span>Client Care</span><span>Contact Us</span></nav>
  <div class="abs footer-social"><i></i><i></i><i></i><i></i><i></i><i></i></div>
  <div class="abs to-top"><svg width="40" height="40" viewBox="0 0 40 40"><path d="M20 30V10M13 17l7-7 7 7" stroke="#43a03a" stroke-width="2" fill="none"/></svg></div>
</footer>

</body>
</html>
```